Establishing a website for a non profit organisation

The foundation is called:

German: Edle Alte Bruderschaft des Hofes Lindenmark e.V.

Englisch (Translation): Noble old Brotherhood of Court Lindenmark e.V.

The foundation is a legal nonprofit organization with the purpose to help people in need. The foundation - a charitable organization - donates funds and supports solely and directly people living in Frankfurt and in Germany.

In some cases the foundation works together with other charitable organizations that support projects to help people in need.

The foundation also functions as trustee with powers of administration of property in trust with a legal obligation to administer it solely for the purposes specified. The purpose is not to generate/obtain wealth for shareholders but to respectfully execute the benevolent intentions of the founders/testators in the interest of the legatee.

The foundation was established in 1408.

The website should give a good and easy overview about the foundation work.
It should be easy to figure out how to participate and help the organisation.
Either you can participate with a one time donation, with a regular donation or with a testament.

For those with donation it is possible to hand over an contribution receipt for tax purposes.

The main color should be red: RGB R:229 - G:47 - B:34

```html
<!DOCTYPE html>
<html lang="en">
<head>
<meta charset="utf-8">
<title>Edle Alte Bruderschaft des Hofes Lindenmark e.V.</title>
<link href="https://fonts.googleapis.com/css2?family=Lato:wght@400;700&display=swap" rel="stylesheet">
<style>
  :root {
    --page-bg: #ebebeb;
    --panel: #ffffff;
    --title: #555555;
    --body: #9a9a9a;
    --link: #3b7fd9;
    --rule: #e2e2e2;
    --brand-red: #e52f22;
    --footer-bg: #3b3b3b;
    --footer-dark: #2b2b2b;
    --footer-head: #ffffff;
    --footer-link: #7a7a7a;
    --join: #bdbdbd;
    --muted: #8a8a8a;
  }
  * { box-sizing: border-box; margin: 0; padding: 0; }
  html, body { width: 1200px; height: 900px; overflow: hidden; }
  body {
    position: relative;
    background: var(--page-bg);
    font-family: "Lato", Arial, sans-serif;
  }
  .news-panel {
    position: absolute; left: 35px; top: 0; width: 765px; height: 585px;
    background: var(--panel);
  }
  .article { position: absolute; left: 44px; width: 680px; }
  .article-title {
    font-size: 18px; font-weight: 700; color: var(--title); line-height: 22px;
  }
  .article-text {
    width: 530px; margin-top: 9px;
    font-size: 16.4px; line-height: 20px; color: var(--body);
  }
  .read-more {
    display: block; margin-top: 10px;
    font-size: 16px; font-weight: 700; color: var(--link); text-decoration: none;
  }
  .article-photo {
    position: absolute; left: 559px; width: 117px; height: 117px;
  }
  .divider {
    position: absolute; left: 51px; width: 676px; height: 1px; background: var(--rule);
  }
  .video-panel {
    position: absolute; left: 812px; top: 0; width: 353px; height: 235px;
    background: var(--panel);
  }
  .video-frame {
    position: absolute; left: 28px; top: 0; width: 299px; height: 190px; overflow: hidden;
  }
  .video-still {
    position: absolute; inset: 0;
    background: linear-gradient(160deg, #a8a39b 0%, #6e6258 55%, #3c3a3a 100%);
  }
  .video-controls { position: absolute; left: 0; bottom: 0; width: 299px; height: 36px; }
  .more-from {
    position: absolute; right: 26px; top: 202px;
    font-size: 14px; font-weight: 700; color: var(--link);
  }
  .tweets-panel {
    position: absolute; left: 812px; top: 248px; width: 353px; height: 337px;
    background: var(--panel);
  }
  .tweets-heading {
    position: absolute; left: 29px; top: 13px;
    font-size: 22px; font-weight: 700; color: var(--brand-red);
  }
  .tweet-rule { position: absolute; left: 29px; width: 289px; height: 1px; background: var(--rule); }
  .tweet { position: absolute; left: 29px; width: 300px; }
  .tweet-mark {
    position: absolute; left: 2px; top: 6px; width: 28px; height: 22px;
    border-radius: 50%; background: #2da6e6;
  }
  .tweet-text {
    margin-left: 43px; width: 248px;
    font-size: 16.2px; line-height: 20px; color: var(--body);
  }
  .site-footer {
    position: absolute; left: 0; top: 617px; width: 1200px; height: 238px;
    background: var(--footer-bg);
    box-shadow: 0 3px 5px rgba(0,0,0,0.35);
  }
  .footer-col { position: absolute; top: 27px; }
  .footer-col h3 {
    font-size: 21px; font-weight: 700; color: var(--footer-head); line-height: 26px;
  }
  .footer-col a {
    display: block; margin-top: 19px;
    font-size: 18px; font-weight: 700; color: var(--footer-link); text-decoration: none; line-height: 26px;
  }
  .footer-col h3 + a { margin-top: 17px; }
  .footer-divider {
    position: absolute; left: 799px; top: 8px; width: 2px; height: 218px; background: #262626;
  }
  .footer-heading {
    position: absolute; left: 838px;
    font-size: 22px; font-weight: 700; color: var(--footer-head);
  }
  .newsletter {
    position: absolute; left: 831px; top: 56px; width: 331px; height: 54px;
    background: var(--footer-dark); border-radius: 2px;
  }
  .newsletter-field {
    position: absolute; left: 24px; top: 15px;
    font-size: 18px; color: var(--muted);
  }
  .newsletter-join {
    position: absolute; left: 259px; top: 9px; width: 65px; height: 38px;
    background: var(--join); border-radius: 2px;
    font-size: 18px; color: #444; text-align: center; line-height: 38px;
  }
  .social-link {
    position: absolute; top: 161px; width: 47px; height: 47px;
    background: var(--footer-dark); border-radius: 3px;
    box-shadow: 1px 2px 2px rgba(0,0,0,0.4);
  }
  .social-link span {
    position: absolute; left: 14px; top: 14px; width: 19px; height: 19px;
    border-radius: 50%; background: #f2f2f2;
  }
  .copyright {
    position: absolute; left: 0; top: 862px; width: 1200px; text-align: center;
    font-size: 14px; color: var(--muted);
  }
</style>
</head>
<body>
  <section class="news-panel">
    <article class="article" style="top:-8px">
      <h2 class="article-title">Consectetur adipisicing elit, sed do eiusmod tempor</h2>
      <p class="article-text">Proin gravida nibh vel velit auctor aliquet. Aenean sollicitudin, lorem quis bibendum auctor, Duis sed odio sit amet nibh vulputate cursus a sit amet mauris. Morbi accumsan ipsum velit. Nam nec tellus a odio tincidunt auctor a ornare odio.</p>
      <a class="read-more" href="#">Read more...</a>
      <div class="article-photo" role="img" aria-label="Children sitting together at a community workshop" style="top:8px;background:linear-gradient(150deg,#8c7b73,#4f4a55 60%,#a28570)"></div>
    </article>
    <div class="divider" style="top:167px"></div>

    <article class="article" style="top:205px">
      <h2 class="article-title">Eiusmod tempor incididunt ut labore et dolore magna</h2>
      <p class="article-text">Proin gravida nibh vel velit auctor aliquet. Aenean sollicitudin, lorem quis bibendum auctor, Duis sed odio sit amet nibh vulputate cursus a sit amet mauris. Morbi accumsan ipsum velit. Nam nec tellus a odio tincidunt auctor a ornare odio.</p>
      <a class="read-more" href="#">Read more...</a>
      <div class="article-photo" role="img" aria-label="Two children walking together in a camp" style="top:7px;background:linear-gradient(160deg,#8a8c8f,#6a5544 55%,#7b5f4a)"></div>
    </article>
    <div class="divider" style="top:381px"></div>

    <article class="article" style="top:417px">
      <h2 class="article-title">Lorem ipsum dolor sit amet constra de amor</h2>
      <p class="article-text">Proin gravida nibh vel velit auctor aliquet. Aenean sollicitudin, lorem quis bibendum auctor, Duis sed odio sit amet nibh vulputate cursus a sit amet mauris. Morbi accumsan ipsum velit. Nam nec tellus a odio tincidunt auctor a ornare odio.</p>
      <a class="read-more" href="#">Read more...</a>
      <div class="article-photo" role="img" aria-label="Girl drinking fresh water from a tap" style="top:7px;background:linear-gradient(160deg,#6b4a2e,#3f6a66 55%,#2f5a5a)"></div>
    </article>
  </section>

  <aside class="video-panel">
    <div class="video-frame">
      <div class="video-still" role="img" aria-label="Video message from a foundation speaker"></div>
      <svg width="299" height="190" viewBox="0 0 299 190" style="position:absolute;left:0;top:0">
        <circle cx="150" cy="70" r="21" fill="rgba(20,20,20,0.85)"/>
        <path d="M144 60 L160 70 L144 80 Z" fill="#fff"/>
      </svg>
      <svg class="video-controls" viewBox="0 0 299 36">
        <rect width="299" height="36" fill="#1b1b1b"/>
        <rect x="0" y="3" width="299" height="4" fill="#444"/>
        <circle cx="6" cy="5" r="4" fill="#ddd"/>
        <path d="M14 16 L22 21 L14 26 Z" fill="#bbb"/>
        <rect x="43" y="17" width="2" height="8" fill="#bbb"/><path d="M52 17 L46 21 L52 25 Z" fill="#bbb"/>
        <path d="M64 17 L70 21 L64 25 Z" fill="#bbb"/><rect x="70" y="17" width="2" height="8" fill="#bbb"/>
        <path d="M83 19 h3 l4 -3 v10 l-4 -3 h-3 Z" fill="#bbb"/>
        <text x="108" y="24" font-family="Lato, sans-serif" font-size="8" fill="#ddd">0:00 / 3:15</text>
        <circle cx="212" cy="21" r="4" fill="#bbb"/>
        <rect x="228" y="18" width="9" height="6" fill="#777"/>
        <rect x="250" y="17" width="22" height="8" fill="#555"/>
        <rect x="282" y="16" width="10" height="10" fill="none" stroke="#bbb" stroke-width="1.2"/>
      </svg>
    </div>
    <div class="more-from">More from ClipStream</div>
  </aside>

  <aside class="tweets-panel">
    <h2 class="tweets-heading">Latest Tweets</h2>
    <div class="tweet-rule" style="top:53px"></div>
    <div class="tweet" style="top:74px">
      <span class="tweet-mark"></span>
      <p class="tweet-text">This is Pixelforge's version of Lorem Ipsum. Proin gravida nibh vel velit ....</p>
    </div>
    <div class="tweet-rule" style="top:149px"></div>
    <div class="tweet" style="top:163px">
      <span class="tweet-mark"></span>
      <p class="tweet-text">sed do eiusmod tempor incididunt ut labore et dolore magna aliqua. Ut enim ad minim veniam ....</p>
    </div>
    <div class="tweet-rule" style="top:239px"></div>
    <div class="tweet" style="top:255px">
      <span class="tweet-mark"></span>
      <p class="tweet-text">Duis aute irure dolor in reprehen-derit in voluptate velit esse cillum dolore eu fugiat ....</p>
    </div>
  </aside>

  <footer class="site-footer">
    <nav class="footer-col" style="left:75px">
      <h3>connect</h3>
      <a href="#">contact info</a><a href="#">512.34.806</a><a href="#">FAQs</a>
    </nav>
    <nav class="footer-col" style="left:234px">
      <h3>about us</h3>
      <a href="#">annual report</a><a href="#">in-kind donors</a><a href="#">press</a>
    </nav>
    <nav class="footer-col" style="left:412px">
      <h3>resources</h3>
      <a href="#">download assets</a><a href="#">request a speaker</a><a href="#">fundraiser toolkit</a>
    </nav>
    <nav class="footer-col" style="left:635px">
      <h3>get involved</h3>
      <a href="#">fundraise</a><a href="#">donate</a><a href="#">volunteer</a>
    </nav>
    <div class="footer-divider"></div>
    <h3 class="footer-heading" style="top:23px">Subcribe Newsletter</h3>
    <div class="newsletter">
      <span class="newsletter-field">Join our mailing list</span>
      <span class="newsletter-join">Join</span>
    </div>
    <h3 class="footer-heading" style="top:118px">Our Community</h3>
    <a class="social-link" href="#" aria-label="Community network one" style="left:835px"><span></span></a>
    <a class="social-link" href="#" aria-label="Community network two" style="left:894px"><span></span></a>
    <a class="social-link" href="#" aria-label="Community network three" style="left:954px"><span></span></a>
    <a class="social-link" href="#" aria-label="Community network four" style="left:1013px"><span></span></a>
  </footer>

  <p class="copyright">© 2014 Edle Alte Bruderschaft des Hofes Lindenmark e.V.&nbsp; All right reserved.</p>
</body>
</html>
```